New small country town business wanting to expand online wants a website to do sales, post local ...

Our logo was designed through Pixel Harbor and we loved it. We would like a website designed for us. We want to be able to sell things online, manage the upkeep ourselves, have a separate page that we can advertise local businesses, a page that contains local information and events, local Buy, sell or swap page, promote tourism in our local area, chat with us. We use Quickbooks and Square We also have a local business Tallowind Creek Cruises - see our website for that www.tallowindcreekcruises.com.au which we promote through our shop 'The Reel Hut'. The Reel Hut sells, hot pies, fishing tackle, bait, groceries, boating accessories, souvenir T-Shirts (also designed by Pixel Harbor) etc. Do you set it up? Do I need to get the hosting done? I dont understand what coding the website means. I apologise for my ignorance. We sell coffee and newspapers to the locals. Provide a meeting place in a town where the only other shop here actively discourages and often verbally abuses the locals.Maree
I apologise for the delay, my father is in hospital and is gravely ill. I have had to fly to Perth to be with him . Can I please have a 2 week extension? Thank you. Mar ee

```html
<!DOCTYPE html>
<html lang="en">
<head>
<meta charset="utf-8">
<title>The Reel Hut</title>
<link href="https://fonts.googleapis.com/css2?family=Nunito:wght@400;600;700&display=swap" rel="stylesheet">
<style>
:root{
  --pink:#ee1c8a;
  --ink:#222630;
  --text:#333;
  --muted:#555;
  --line:#cfd3d8;
  --soft:#f6f7f9;
  --link:#2a6fdb;
  --white:#fff;
}
*{box-sizing:border-box;margin:0;padding:0}
html,body{width:1200px;height:3764px;overflow:hidden}
body{position:relative;background:var(--white);font-family:'Nunito',sans-serif;color:var(--text)}
.abs{position:absolute}
.accent{color:var(--pink)}
.brand{display:flex;align-items:center;gap:14px;font-weight:700;font-size:40px;color:#1f2a6b}
.brand .dot{width:30px;height:30px;border-radius:50%;background:#c8102e}
.site-header .brand{left:16px;top:28px}
.main-nav{right:16px;top:46px;display:flex;gap:17px;font-size:17px;color:var(--ink)}
.main-nav .current{color:var(--pink)}
.hero{left:4px;top:123px;width:1187px;height:847px;
  background:linear-gradient(180deg,#c9d2dc 0%,#aab6c3 35%,#3f4a35 48%,#6b7560 55%,#a9b3bd 75%,#8e98a3 100%)}
.hero-copy{left:183px;top:466px;width:830px;color:var(--white)}
.hero-copy .kicker{font-size:20px;font-weight:600}
.hero-copy h1{font-size:42px;font-weight:700;margin:8px 0 10px}
.hero-copy p{font-size:16px;line-height:1.55}
.btn{display:inline-block;background:var(--pink);color:var(--white);font-size:16px;padding:6px 14px}
.hero-copy .btn{margin-top:18px}
.hero-arrow{top:553px;width:20px;height:20px}
.about-photo{left:7px;top:1019px;width:476px;height:285px;background:linear-gradient(180deg,#e9f1f4 0%,#7e9b5a 30%,#4d6b34 55%,#6e8a55 75%,#3f5a2e 100%)}
.about-copy{left:515px;top:1019px;width:665px}
.eyebrow{font-size:25px;font-weight:600;color:var(--ink)}
.about-copy h2{font-size:42px;font-weight:600;line-height:1.25;margin:14px 0 14px;color:var(--ink)}
.body-text{font-size:16px;line-height:1.6;color:var(--text)}
.events-copy{left:8px;top:1365px;width:680px}
.events-copy h2{font-size:30px;font-weight:600;color:var(--ink);margin:8px 0 12px}
.video{left:718px;top:1365px;width:476px;height:239px;background:linear-gradient(180deg,#1c1c1c,#2b2b2b 70%,#111)}
.video .bar{left:18px;right:18px;bottom:20px;height:3px;background:#777}
.video .time{left:51px;bottom:40px;color:#ddd;font-size:15px}
.contact-head{left:0;top:1688px;width:1200px;text-align:center}
.contact-head h2{font-size:36px;font-weight:600;color:var(--ink)}
.contact-head p{font-size:16px;line-height:1.6;margin-top:8px;color:var(--text)}
.locations{left:15px;top:1805px}
.loc{display:flex;gap:18px;margin-bottom:26px}
.loc .icon{width:52px;height:52px;border:2px solid var(--ink);display:flex;align-items:center;justify-content:center;margin-top:12px}
.loc p{font-size:16px;line-height:1.55}
.loc .title{font-weight:600;color:var(--ink)}
.contact-form{left:609px;top:1805px;width:576px}
.field{height:40px;border:1px solid var(--line);border-radius:3px;margin-bottom:9px;padding:9px 12px;font-size:16px;color:#666}
.field.area{height:104px;padding:42px 50px}
.contact-form .btn{position:absolute;left:247px;top:259px;padding:6px 12px}
.places-title{left:0;top:2145px;font-size:42px;font-weight:600;color:var(--ink)}
.tile{top:2217px;width:368px;height:245px}
.products{left:6px;top:2498px;width:1187px;height:847px;background:var(--soft)}
.products-head{left:0;top:2552px;width:1200px;text-align:center}
.products-head h2{font-size:44px;font-weight:600;color:var(--ink)}
.products-head p{font-size:16px;line-height:1.6;margin-top:8px}
.filters{left:0;top:2681px;width:1200px;display:flex;justify-content:center;gap:12px}
.filters span{border:1px solid var(--line);background:var(--white);padding:4px 6px;font-size:16px;color:var(--ink)}
.filters .on{background:var(--pink);color:var(--white);border-color:var(--pink)}
.product{width:369px}
.site-footer .brand{left:48px;top:3392px}
.footer-about{left:48px;top:3488px;width:530px}
.footer-about a{display:block;color:var(--link);margin-top:18px;font-size:16px}
.footer-col h3{font-size:25px;font-weight:600;color:var(--ink);margin-bottom:10px}
.footer-links{left:632px;top:3382px}
.footer-links ol{padding-left:24px;font-size:16px;line-height:1.6;color:var(--link)}
.footer-contact{left:826px;top:3382px}
.socials{display:flex;gap:22px;align-items:center;padding-left:4px}
.socials i{display:block;width:14px;height:14px;background:var(--ink)}
.socials i.round{border-radius:50%;background:none;border:2px solid var(--ink)}
.divider{left:16px;top:3681px;width:1184px;height:1px;background:#ddd}
.copyright{left:48px;top:3712px;font-size:16px;color:var(--ink)}
</style>
</head>
<body>
<header class="site-header">
  <div class="abs brand"><span class="dot"></span>The Reel Hut</div>
  <nav class="abs main-nav"><span class="current">Home</span><span>About</span><span>Events</span><span>Our Accessories</span><span>Contact</span></nav>
</header>

<section class="abs hero" role="img" aria-label="Calm river reflecting cloudy sky and forested hills"></section>
<svg class="abs hero-arrow" style="left:84px" viewBox="0 0 20 20"><path d="M13 3 6 10l7 7" fill="none" stroke="#fff" stroke-width="3"/></svg>
<svg class="abs hero-arrow" style="left:1092px" viewBox="0 0 20 20"><path d="M7 3l7 7-7 7" fill="none" stroke="#fff" stroke-width="3"/></svg>
<div class="abs hero-copy">
  <div class="kicker">Awesome Attractive places</div>
  <h1>The <span class="accent">Reel</span> Hut</h1>
  <p>Lorem ipsum dolor sit amet, consectetur adipisicing elit. Reprehenderit dolore culpa incidunt veniam eaque,<br>optio beatae, animi eligendi omnis recusandae.</p>
  <span class="btn">Read more</span>
</div>

<div class="abs about-photo" role="img" aria-label="Wooded riverbank reflected in still water"></div>
<section class="abs about-copy">
  <div class="eyebrow">About</div>
  <h2>Tallowind <span class="accent">creek is very beautiful Place</span></h2>
  <p class="body-text">Lorem ipsum dolor sit amet, consectetur adipisicing elit. Accusamus doloribus, delectus optio repellat libero rem corrupti doloremque nisi ut incidunt autem dolorem possimus, aliquam enim consequuntur officia, molestiae esse dicta suscipit ullam cum illo quo. Tempora cupiditate nobis expedita, provident saepe quod aperiam, illo harum reiciendis alias illum obcaecati natus!</p>
</section>

<section class="abs events-copy">
  <div class="eyebrow">Activities</div>
  <h2>Local Events</h2>
  <p class="body-text">We then fully customize the raw footage by adding content/text on top of each transition/segment within the video ad. The transition/segment is basically every time the text or an image or both change within the video.<br>When a business signs up for a video mockup with us, we search our library for specific types of footage and images that fit the product and services that you want to promote, or according to the specific detailed instructions from the client.</p>
</section>
<div class="abs video">
  <svg class="abs" style="left:22px;bottom:40px" width="12" height="14" viewBox="0 0 12 14"><path d="M1 1l10 6-10 6z" fill="#aaa"/></svg>
  <span class="abs time">0:00</span>
  <svg class="abs" style="right:96px;bottom:42px" width="18" height="14" viewBox="0 0 18 14"><path d="M1 4h4l5-4v14l-5-4H1z" fill="#aaa"/></svg>
  <svg class="abs" style="right:40px;bottom:42px" width="14" height="14" viewBox="0 0 14 14"><path d="M1 5V1h4M9 1h4v4M13 9v4H9M5 13H1V9" fill="none" stroke="#aaa" stroke-width="1.5"/></svg>
  <div class="abs bar"></div>
</div>

<section class="abs contact-head">
  <h2><span class="accent">Contact</span> Us</h2>
  <p>Lorem ipsum dolor sit amet, consectetur adipisicing elit. Voluptatem asperiores nihil,<br>tempora saepe vel veritatis dignissimos laudantium distinctio error architecto.</p>
</section>
<div class="abs locations">
  <div class="loc"><span class="icon"><svg width="26" height="30" viewBox="0 0 26 30"><path d="M13 29S3 17 3 11a10 10 0 0 1 20 0c0 6-10 18-10 18z" fill="none" stroke="#222630" stroke-width="2.5"/><circle cx="13" cy="11" r="4" fill="#222630"/></svg></span><p><span class="title">Our location</span><br>14/c riverside house<br>Ferry lane Tallowind</p></div>
  <div class="loc"><span class="icon"><svg width="26" height="30" viewBox="0 0 26 30"><path d="M13 29S3 17 3 11a10 10 0 0 1 20 0c0 6-10 18-10 18z" fill="none" stroke="#222630" stroke-width="2.5"/><circle cx="13" cy="11" r="4" fill="#222630"/></svg></span><p><span class="title">Our location</span><br>14/c riverside house<br>Ferry lane Tallowind</p></div>
  <div class="loc"><span class="icon"><svg width="26" height="30" viewBox="0 0 26 30"><path d="M13 29S3 17 3 11a10 10 0 0 1 20 0c0 6-10 18-10 18z" fill="none" stroke="#222630" stroke-width="2.5"/><circle cx="13" cy="11" r="4" fill="#222630"/></svg></span><p><span class="title">Our location</span><br>14/c riverside house<br>Ferry lane Tallowind</p></div>
</div>
<form class="abs contact-form">
  <div class="field">Your Name</div>
  <div class="field">Your Email</div>
  <div class="field">Your Subject</div>
  <div class="field area">Write your name</div>
  <span class="btn">Submit</span>
</form>

<h2 class="abs places-title">Beatiful <span class="accent">Places</span></h2>
<div class="abs tile" style="left:10px;background:linear-gradient(180deg,#e6e2e0 0%,#3d4a33 40%,#28321f 60%,#8f979c 75%,#a4aab0 100%)" role="img" aria-label="Forested shoreline beside a grey river"></div>
<div class="abs tile" style="left:400px;background:linear-gradient(180deg,#a9c1cf 0%,#3f7a86 30%,#45706b 55%,#3b8a8e 100%)" role="img" aria-label="Aerial view of river inlets and islands"></div>
<div class="abs tile" style="left:789px;background:linear-gradient(180deg,#1f4fbf 0%,#6d9ee0 45%,#4d7d4a 52%,#2f62b8 70%,#1d49a8 100%)" role="img" aria-label="Wooden jetty stretching across a blue lake"></div>

<section class="abs products"></section>
<div class="abs products-head">
  <h2>Our <span class="accent">products</span></h2>
  <p>Lorem ipsum dolor sit amet, consectetur adipisicing elit. Sed tempore quae est odio,<br>eos impedit ex eum tenetur necessitatibus praesentium!</p>
</div>
<div class="abs filters"><span class="on">All</span><span>Hot Pie</span><span>Fishing Tackle</span><span>T-shirt</span><span>Grocceries</span></div>
<div class="abs product" style="left:16px;top:2725px;height:287px;background:radial-gradient(ellipse at 50% 45%,#d9913f 0%,#c27a32 40%,#f2efe9 62%,#6b3b1c 100%)" role="img" aria-label="Golden hot pie on a plate"></div>
<div class="abs product" style="left:405px;top:2725px;height:320px;background:linear-gradient(135deg,#f3f4f6 0%,#e9eaec 50%,#f3f4f6 100%)" role="img" aria-label="Fishing rod with reel"></div>
<div class="abs product" style="left:795px;top:2725px;height:287px;background:radial-gradient(ellipse at 50% 40%,#d99a2b 0%,#f3f4f6 45%)" role="img" aria-label="Orange fishing lure with hooks"></div>
<div class="abs product" style="left:16px;top:3032px;height:287px;background:linear-gradient(180deg,#6f9b4a 0%,#d8392b 30%,#e4b32e 50%,#c8322a 70%,#4f8a3a 100%)" role="img" aria-label="Shelves of fresh vegetables"></div>
<div class="abs product" style="left:405px;top:3065px;height:280px;background:radial-gradient(ellipse at 50% 50%,#1f1f1f 0%,#1c1c1c 55%,#eeeff1 70%)" role="img" aria-label="Black souvenir T-shirt"></div>
<div class="abs product" style="left:795px;top:3032px;height:287px;background:linear-gradient(135deg,#eef0f3 0%,#c9ccd1 40%,#e4553f 70%,#f2f3f5 100%)" role="img" aria-label="Assorted boating accessories"></div>

<footer class="site-footer">
  <div class="abs brand"><span class="dot"></span>The Reel Hut</div>
  <div class="abs footer-about body-text">Lorem ipsum dolor sit amet, consectetur adipisicing elit. Maxime accusamus mollitia dicta enim vel velit, animi, assumenda perferendis fugit quos corporis architecto distinctio recusandae esse voluptatem nobis eligendi. Modi omnis aliquam doloribus natus, necessitatibus rerum, repudiandae maiores deserunt voluptatum minus.<a>Read More</a></div>
  <div class="abs footer-col footer-links"><h3>Helpful-links</h3><ol><li>lorem ipsum</li><li>lorem ipsum</li><li>lorem ipsum</li><li>lorem ipsum</li><li>lorem ipsum</li></ol></div>
  <div class="abs footer-col footer-contact"><h3>contact us</h3>
    <div class="socials"><i></i><i class="round"></i><svg width="16" height="16" viewBox="0 0 16 16"><path d="M3 1l3 3-2 2c1 2 3 4 5 5l2-2 3 3-2 3C7 15 1 9 1 3z" fill="#222630"/></svg><i></i></div>
  </div>
  <div class="abs divider"></div>
  <p class="abs copyright">COPYRIGHT 2017 The Reel Hut | ALL RIGHTS RESERVED</p>
</footer>
</body>
</html>
```